Create a 3-4 page concept for an electrical contracting company

We are a company that requires a new look for our website. We are familiar with Sitecraft to be able to update using any theme or builder supplied.

While typical ideas of construction may get the yellow and blue colour pallette, hard hats, hammers, or lightning bolts entering the arena, we are completely against this image.

We intend for the website to have instant appeal and intuitive navigation. The home page should have a creative use of angles or brand identification with the banner or menubar if needed.

After combing hundreds of sitecraft templates, the most attractive seem to be aimed at beauty services. Unfortunately we do not have a lot of picture perfect material to showcase, but it can be blended in other ways. - the brand should be recognizable and captivating.

Target Market(s)

High-end contracting firms focused on quality and service for long term projects (Custom Homes)

Industry/Entity Type

Contracting

Font styles to use
Sans Serif
Other font styles liked:
• Gotham usually. Adjusted kerning and rounded edges seem to be more friendly

Requirements
Must have
• Creative use of the logo shape and colour scheme, especially at the home.

Use of a CMS to be modifiable from a browser (Sitecraft,etc) - A builder such as tandem, kora, or framewell accepted!

Elements or sections that could be adaptable for use. About us, members, contact, services... etc. Content would be written after
Nice to have
• Some clean inspiration that we appreciate:

www.harbelmedia.ca
www.pinwoodbuildworks.com
Should not have
• Generic welcome banner...

```html
<!DOCTYPE html>
<html lang="en">
<head>
<meta charset="utf-8">
<title>Bastion Electric</title>
<link href="https://fonts.googleapis.com/css2?family=Ubuntu:wght@400;500;700&family=Open+Sans:wght@300;400;600;700&display=swap" rel="stylesheet">
<style>
:root{
  --steel:#2c4560;
  --steel-deep:#1b2c40;
  --steel-mid:#3a5775;
  --slate:#3d5c7c;
  --ink:#2a2f38;
  --muted:#8a8f98;
  --body:#70757e;
  --light:#f2f3f5;
  --white:#ffffff;
  --accent:#8fb3c9;
  --green:#2f5d50;
  --star:#c9a66b;
}
*{margin:0;padding:0;box-sizing:border-box}
html,body{width:1200px;height:5342px;overflow:hidden}
body{position:relative;background:var(--white);font-family:"Open Sans",sans-serif;color:var(--ink)}
.abs{position:absolute}
h1,h2,h3,.heading{font-family:"Ubuntu",sans-serif}
.body-copy{font-weight:300;color:var(--muted);font-size:17px;line-height:32px}

/* hero */
.hero{left:0;top:0;width:1200px;height:736px;
  background:
    linear-gradient(118deg,rgba(255,255,255,0) 0 52%,rgba(143,179,201,.14) 52% 70%,rgba(255,255,255,0) 70%),
    linear-gradient(62deg,rgba(0,0,0,0) 0 60%,rgba(0,0,0,.18) 60%),
    linear-gradient(115deg,#24384f 0%,#34506d 50%,#1d2e42 100%)}
.brand{display:flex;align-items:center;gap:12px;color:var(--white);font-family:"Ubuntu",sans-serif;font-weight:500;font-size:20px;line-height:19px;letter-spacing:1px}
.brand-dot{width:34px;height:34px;background:var(--white);border-radius:4px}
.nav{top:36px;left:382px;display:flex;gap:60px;font-size:12px;font-weight:600;color:var(--white);letter-spacing:.5px}
.cta{left:921px;top:24px;width:166px;height:42px;border:2px solid var(--white);color:var(--white);font-size:12px;font-weight:700;letter-spacing:.5px;display:flex;align-items:center;justify-content:center}
.hero-title{left:114px;top:318px;color:var(--white);font-weight:700;font-size:52px;line-height:62px;text-transform:uppercase}
.hero-sub{left:114px;top:450px;color:var(--white);font-size:25px;font-weight:400}
.hero-contact{left:890px;top:668px;color:var(--white);display:flex;gap:10px;align-items:center}
.hero-contact .num{font-family:"Ubuntu",sans-serif;font-size:24px;font-weight:500}
.hero-contact .mail{font-size:11px}

/* about */
.about-photo{left:114px;top:674px;width:390px;height:431px;background:linear-gradient(160deg,#f3f4f6,#c9ced6 60%,#e6e8ec);box-shadow:0 20px 40px rgba(0,0,0,.15)}
.section-title{font-size:50px;font-weight:500;color:var(--ink)}

/* features */
.feature{top:1265px;width:230px}
.feature h3{font-size:26px;font-weight:500;margin:28px 0 12px;line-height:32px;white-space:nowrap}
.feature p{font-weight:300;color:var(--muted);font-size:17px;line-height:31px}
.feature-card{left:336px;top:1240px;width:276px;height:366px;background:var(--white);box-shadow:0 10px 35px rgba(0,0,0,.1)}

/* banner */
.banner{left:0;top:1710px;width:1200px;height:698px;background:linear-gradient(180deg,#ffffff 0%,#5b6f92 14%,#2b3b5f 55%,#1b263e 100%)}
.banner-frame{left:60px;top:1790px;width:1104px;height:580px;border-right:3px solid var(--white);border-bottom:3px solid var(--white)}
.banner-box{left:589px;top:2222px;width:541px;height:147px;background:rgba(22,30,52,.85);color:var(--white);font-family:"Ubuntu",sans-serif;font-weight:500;font-size:30px;line-height:42px;padding:30px 0 0 34px;text-transform:uppercase}

/* ready */
.ready{left:0;top:2408px;width:1200px;height:929px;background:var(--light)}
.ready-title{left:116px;top:2504px;font-size:52px;line-height:64px;font-weight:500}
.ready-rule{left:503px;top:2520px;width:2px;height:108px;background:#c7cad0}
.service{top:2698px;width:307px;height:552px}
.service.raised{background:var(--white);box-shadow:0 10px 30px rgba(0,0,0,.1)}
.service .img{width:307px;height:265px}
.service h3{font-size:27px;font-weight:500;margin:36px 0 14px 24px}
.service p{margin:0 24px;font-weight:300;color:var(--body);font-size:18px;line-height:31px}
.service a{color:var(--body);font-size:18px}

/* projects */
.project-side{left:0;top:3337px;width:363px;height:704px;background:var(--slate)}
.project-photo{left:363px;top:3337px;width:837px;height:704px;background:radial-gradient(ellipse at 40% 90%,#f3e6c2 0%,#8a6e3c 20%,#3a3025 55%,#1c1a18 100%)}
.project-side h2{position:absolute;left:111px;top:100px;color:var(--white);font-size:52px;line-height:62px;font-weight:700}
.project-side .item{position:absolute;left:111px;color:var(--white);font-size:19px}

/* testimonial */
.say-title{left:0;top:4150px;width:1200px;text-align:center;font-size:52px;font-weight:500}
.avatar{left:503px;top:4276px;width:194px;height:194px;border-radius:50%;background:radial-gradient(circle at 50% 40%,#cfd6de,#8a9aab)}
.person{left:0;width:1200px;text-align:center}
.quote{left:0;top:4618px;width:1200px;text-align:center;font-weight:300;color:var(--green);font-size:17px;line-height:32px}
.partners{left:130px;top:4838px;width:940px;display:flex;justify-content:space-between;align-items:center;font-family:"Ubuntu",sans-serif;font-weight:500;font-size:22px;color:#333}

/* footer */
.footer{left:0;top:4943px;width:1200px;height:399px;background:var(--slate)}
.footer .center{position:absolute;left:0;width:1200px;text-align:center;color:var(--white);font-size:15px}
.socials{display:flex;justify-content:center;gap:26px}
.socials span{width:18px;height:18px;border-radius:50%;background:var(--white)}
.footer-rule{left:116px;top:315px;width:968px;height:1px;background:rgba(255,255,255,.35)}
</style>
</head>
<body>

<!-- hero -->
<section class="abs hero" role="img" aria-label="Photo of an electrician working at a switchboard, steel blue tone"></section>
<div class="abs brand" style="left:114px;top:22px"><span class="brand-dot"></span><span>BASTION<br>ELECTRIC</span></div>
<nav class="abs nav"><span>ABOUT US</span><span>MEMBERS</span><span>CONTACT</span><span>SERVICES</span></nav>
<div class="abs cta">GET IN TOUCH</div>
<h1 class="abs hero-title">Electricity<br>for your home</h1>
<p class="abs hero-sub">- ENERGY FOR LIVING</p>
<div class="abs hero-contact">
  <svg width="34" height="34" viewBox="0 0 24 24" fill="none" stroke="#fff" stroke-width="1.8"><path d="M5 3h4l2 5-2.5 1.5a11 11 0 0 0 6 6L16 13l5 2v4a2 2 0 0 1-2 2A17 17 0 0 1 3 5a2 2 0 0 1 2-2z"/></svg>
  <div><div class="num">01-5550-2719</div><div class="mail">hello@bastionelectric.com</div></div>
</div>

<!-- about -->
<div class="abs about-photo" role="img" aria-label="Photo of a modern electrical ceiling installation in light grey"></div>
<h2 class="abs section-title" style="left:558px;top:790px">Who We Are</h2>
<p class="abs body-copy" style="left:567px;top:882px;width:460px">Pellentesque at tincidunt lorem, sollicitudin eleifend ante. Nunc vestibulum facilisis leo. Mauris iaculis suscipit ligula, nec luctus ligula pulvinar in.</p>

<!-- features -->
<div class="abs feature-card"></div>
<div class="abs feature" style="left:114px">
  <svg width="72" height="64" viewBox="0 0 72 64" fill="none" stroke="#3a5775" stroke-width="2.5"><circle cx="44" cy="26" r="22"/><path d="M24 36h14v14H24z M31 50v10 M10 40h14"/></svg>
  <h3 class="heading">Electricity for life</h3>
  <p>Pellentesque at tincidunt lorem, sollicitudin eleifend ante. Nunc vestibulum facilisis leo.</p>
</div>
<div class="abs feature" style="left:366px;top:1272px;width:220px">
  <svg width="72" height="70" viewBox="0 0 72 70" fill="none" stroke="#3a5775" stroke-width="2.5"><circle cx="36" cy="34" r="32"/><path d="M27 20v10 M45 20v10 M22 30h28v8a14 14 0 0 1-28 0z M36 52v12"/></svg>
  <h3 class="heading" style="margin-top:18px;white-space:normal">Electricity for<br>life</h3>
  <p>Pellentesque at tincidunt lorem, sollicitudin eleifend ante. Nunc vestibulum facilisis leo. Mauris iaculis</p>
</div>
<div class="abs feature" style="left:618px">
  <svg width="68" height="68" viewBox="0 0 68 68" fill="none" stroke="#3a5775" stroke-width="2.5"><circle cx="34" cy="34" r="31"/><rect x="20" y="27" width="28" height="14" rx="7"/><circle cx="40" cy="34" r="4"/></svg>
  <h3 class="heading">Electricity for life</h3>
  <p>Pellentesque at tincidunt lorem, sollicitudin eleifend ante. Nunc vestibulum facilisis leo.</p>
</div>
<div class="abs feature" style="left:866px;top:1280px">
  <svg width="68" height="64" viewBox="0 0 68 64" fill="none" stroke="#3a5775" stroke-width="2.5"><path d="M6 60h56 M14 60V30 M26 60V20 M38 60V24 M50 60V14 M14 30l12-10 12 4 12-10 M10 10h4 M44 6h8"/></svg>
  <h3 class="heading" style="margin-top:14px">Electricity for life</h3>
  <p>Pellentesque at tincidunt lorem, sollicitudin eleifend ante. Nunc vestibulum facilisis leo. Mauris iaculis suscipit ligula, nec luctus ligula</p>
</div>

<!-- banner -->
<section class="abs banner" role="img" aria-label="Night aerial photo of a power plant and city lights"></section>
<div class="abs banner-frame"></div>
<div class="abs banner-box">Build electrical stability<br>to get to your house</div>

<!-- ready -->
<section class="abs ready"></section>
<h2 class="abs ready-title">We are ready<br>to serve you</h2>
<div class="abs ready-rule"></div>
<p class="abs body-copy" style="left:560px;top:2522px;width:520px;color:var(--body)">Mauris iaculis suscipit ligula, nec luctus ligula pulvinar in. Sed eget condimentum quam. Mauris iaculis suscipit ligula, nec luctus ligula pulvinar in. Sed eget condimentum quam.</p>

<article class="abs service raised" style="left:114px">
  <div class="img" role="img" aria-label="Photo of a modern house with solar roof and pool" style="background:linear-gradient(180deg,#b9d3ea,#e9eef2 45%,#5fc7e6 80%)"></div>
  <h3 class="heading">Electricity House</h3>
  <p>Mauris iaculis suscipit ligula, nec luctus ligula pulvinar in. Sed eget condimentum quam.<br><a href="#">more info</a></p>
</article>
<article class="abs service" style="left:446px">
  <div class="img" role="img" aria-label="Photo of a glass house lit warmly at dusk" style="background:linear-gradient(160deg,#4a78b0,#e2a44a 55%,#3a3a3a)"></div>
  <h3 class="heading">Electricity House</h3>
  <p>Mauris iaculis suscipit ligula, nec luctus ligula pulvinar in. Sed eget condimentum quam.<br><a href="#">more info</a></p>
</article>
<article class="abs service" style="left:779px">
  <div class="img" role="img" aria-label="Photo of workers installing solar panels on a red roof" style="background:linear-gradient(150deg,#7fa0b8,#c2504b 50%,#2f3b4b)"></div>
  <h3 class="heading">Electricity House</h3>
  <p>Mauris iaculis suscipit ligula, nec luctus ligula pulvinar in. Sed eget condimentum quam.<br><a href="#">more info</a></p>
</article>

<!-- projects -->
<section class="abs project-side">
  <h2>Our<br>Project</h2>
  <div class="item" style="top:285px;font-weight:700;font-size:19px">San Diego Resort</div>
  <div class="item" style="top:315px;font-size:14px;line-height:22px">Nulla laoreet vestibulum<br>condimentum. <u>more info</u></div>
  <div class="item" style="top:398px">Las Vegas Resort</div>
  <div class="item" style="top:460px">San Fansisco Resort</div>
</section>
<div class="abs project-photo" role="img" aria-label="Photo of a resort terrace with umbrellas and pool lit at night"></div>

<!-- testimonial -->
<h2 class="abs say-title">What They Say</h2>
<svg class="abs" style="left:170px;top:4355px" width="24" height="40" viewBox="0 0 24 40" fill="none" stroke="#2c4560" stroke-width="4"><path d="M20 4 4 20l16 16"/></svg>
<svg class="abs" style="left:1008px;top:4355px" width="24" height="40" viewBox="0 0 24 40" fill="none" stroke="#2c4560" stroke-width="4"><path d="M4 4l16 16L4 36"/></svg>
<div class="abs avatar" role="img" aria-label="Portrait of the client"></div>
<div class="abs person heading" style="top:4492px;font-size:31px;font-weight:500;color:var(--green)">Daniel Reyes</div>
<div class="abs person" style="top:4537px;font-size:17px;color:var(--green)">CEO of Corvel Resort</div>
<div class="abs person" style="top:4562px;font-size:20px;letter-spacing:8px;color:var(--star)">★★★★★</div>
<p class="abs quote">Pellentesque at tincidunt lorem, sollicitudin eleifend ante. Nunc vestibulum facilisis leo.<br>Mauris iaculis suscipit ligula, nec luctus ligula pulvinar in.<br><u>more reviews</u></p>

<div class="abs partners">
  <span>Norvane</span><span>Halden</span><span>Ostrel</span><span>Brivo</span><span>Kelmar</span><span>Tessaro</span>
</div>

<!-- footer -->
<footer class="abs footer">
  <div class="brand" style="position:absolute;left:502px;top:58px;font-size:26px;line-height:25px"><span class="brand-dot" style="width:52px;height:52px"></span><span>BASTION<br>ELECTRIC</span></div>
  <div class="center" style="top:152px">Larkfield Ave. 42, Austin, US</div>
  <div class="center" style="top:178px">p. 01-5550-2719 &nbsp;|&nbsp; e. hello@bastionelectric.com</div>
  <div class="center socials" style="top:213px"><span></span><span></span><span></span><span></span></div>
  <div class="center" style="top:268px">About Us &nbsp;|&nbsp; Members &nbsp;|&nbsp; Contact &nbsp;|&nbsp; Services</div>
  <div class="abs footer-rule"></div>
  <div class="center" style="top:356px;font-size:14px">© 2020. Bastion Electric Company. Alright Reserve.</div>
</footer>

</body>
</html>
```